OAKandRIVER Learning & Development
Business card, Letterhead & Compliment Slip design
Simple
Mara Hollings
Director
41 Fennick Row
Marbury
North Wessex KX4 7RB
mhollings@oakandriverltd-example.co.uk
www.oakandriverltd-example.co.uk
Letterhead needs to be UK standard size A4 and used electronically, therefore, not too heavy on printer toner.
Compliment slip needs to be DL size which is 110mm x 220mm.
We are open to your ideas on this, it could be that the logo is on the front and all other details on reverse side.
We would like to see your ideas please.
Please see attached file for our logo, to be included in this design project. Many thanks.

```html
<!DOCTYPE html>
<html lang="en">
<head>
<meta charset="utf-8">
<title>Oak and River Learning &amp; Development – Stationery</title>
<link rel="stylesheet" href="https://fonts.googleapis.com/css2?family=Montserrat:wght@400;600&display=swap">
<style>
  :root {
    --ink: #0e0e0e;
    --paper: #ffffff;
    --stage: #ffffff;
    --frame: #e4e4e4;
    --gold: #c9a24a;
    --gold-faint: #f1e9da;
    --text-dark: #2a2a2a;
    --text-light: #e8e8e8;
  }
  * { box-sizing: border-box; margin: 0; padding: 0; }
  html, body { width: 1200px; height: 810px; overflow: hidden; background: var(--stage); }
  body { font-family: "Montserrat", sans-serif; position: relative; }

  .sheet-frame {
    position: absolute; left: 18px; top: 28px; width: 1164px; height: 752px;
    border: 1px solid var(--frame);
  }

  .piece { position: absolute; overflow: hidden; box-shadow: 0 1px 3px rgba(0,0,0,.25); }
  .piece--white { background: var(--paper); }
  .piece--black { background: var(--ink); color: var(--text-light); }

  .brand { position: absolute; display: flex; flex-direction: column; align-items: flex-start; }
  .brand__dot { width: 14px; height: 14px; border-radius: 50%; background: var(--gold); margin-bottom: 4px; }
  .brand__name { font-weight: 600; letter-spacing: .02em; line-height: 1; white-space: nowrap; }
  .brand__tagline { font-size: 5px; letter-spacing: .12em; text-transform: uppercase; margin-top: 3px; white-space: nowrap; }
  .brand--dark .brand__name, .brand--dark .brand__tagline { color: var(--ink); }
  .brand--light .brand__name, .brand--light .brand__tagline { color: var(--text-light); }
  .brand--centre { align-items: center; }

  .band { position: absolute; left: 0; top: 0; background: var(--ink); }
  .rule { position: absolute; height: 1px; background: var(--gold); }
  .rule--thick { height: 3px; }
  .rule--ink { background: var(--ink); }

  .faint-circle { position: absolute; border-radius: 50%; background: var(--gold-faint); }

  .contact { position: absolute; font-size: 5px; line-height: 1.55; white-space: nowrap; }
  .contact__name { font-size: 6px; font-weight: 600; }
  .contact__role { margin-bottom: 5px; }
  .contact--dark { color: var(--text-dark); }
  .contact--light { color: var(--text-light); }

  .footer { position: absolute; left: 0; right: 0; font-size: 5px; line-height: 1.6; color: var(--text-dark); text-align: center; white-space: nowrap; }

  .with-compliments { position: absolute; font-size: 11px; letter-spacing: .08em; color: var(--text-dark); white-space: nowrap; }
</style>
</head>
<body>
<div class="sheet-frame"></div>

<section class="piece piece--white card" style="left:96px;top:149px;width:187px;height:108px;">
  <div class="rule rule--thick rule--ink" style="left:120px;top:38px;width:67px;"></div>
  <div class="rule" style="left:120px;top:43px;width:67px;"></div>
  <div class="brand brand--dark" style="left:14px;top:22px;">
    <span class="brand__dot"></span>
    <span class="brand__name" style="font-size:12px;">Oak and River</span>
    <span class="brand__tagline">Learning &amp; Development</span>
  </div>
</section>

<section class="piece piece--black card" style="left:317px;top:149px;width:182px;height:108px;">
  <div class="brand brand--light brand--centre" style="left:0;right:0;top:30px;">
    <span class="brand__dot"></span>
    <span class="brand__name" style="font-size:12px;">Oak and River</span>
    <span class="brand__tagline">Learning &amp; Development</span>
  </div>
  <div class="rule" style="left:0;top:94px;width:182px;"></div>
</section>

<section class="piece piece--white card" style="left:96px;top:281px;width:187px;height:108px;">
  <div class="faint-circle" role="img" aria-label="Faint brand symbol decoration" style="left:122px;top:50px;width:78px;height:78px;"></div>
  <div class="contact contact--dark" style="left:12px;top:14px;">
    <div class="contact__name">Mara Hollings</div>
    <div class="contact__role">Director</div>
    <div>41 Fennick Row, Marbury</div>
    <div>North Wessex KX4 7RB</div>
    <div>Mobile 07000 000000</div>
    <div>mhollings@oakandriverltd-example.co.uk</div>
    <div>www.oakandriverltd-example.co.uk</div>
  </div>
</section>

<section class="piece piece--black card" style="left:317px;top:281px;width:182px;height:108px;">
  <div class="contact contact--light" style="left:12px;top:14px;">
    <div class="contact__name">Mara Hollings</div>
    <div class="contact__role">Director</div>
    <div>41 Fennick Row, Marbury</div>
    <div>North Wessex KX4 7RB</div>
    <div>Mobile 07000 000000</div>
    <div>mhollings@oakandriverltd-example.co.uk</div>
    <div>www.oakandriverltd-example.co.uk</div>
  </div>
  <div class="rule" style="left:0;top:94px;width:182px;"></div>
</section>

<section class="piece piece--white slip" style="left:67px;top:437px;width:437px;height:223px;">
  <div class="band" style="width:437px;height:79px;"></div>
  <div class="rule" style="left:0;top:80px;width:437px;"></div>
  <div class="brand brand--light" style="left:14px;top:26px;">
    <span class="brand__dot"></span>
    <span class="brand__name" style="font-size:14px;">Oak and River</span>
    <span class="brand__tagline">Learning &amp; Development</span>
  </div>
  <div class="faint-circle" role="img" aria-label="Faint brand symbol decoration" style="left:356px;top:90px;width:70px;height:70px;"></div>
  <div class="with-compliments" style="right:24px;top:168px;">WITH COMPLIMENTS</div>
  <div class="footer" style="top:192px;">
    41 Fennick Row · Marbury · North Wessex KX4 7RB · Registered Company no. 0000000<br>
    Phone 01000 000000 · Mobile 07000 000000 · mhollings@oakandriverltd-example.co.uk · www.oakandriverltd-example.co.uk
  </div>
</section>

<section class="piece piece--white letterhead" style="left:583px;top:108px;width:336px;height:655px;">
  <div class="band" style="width:336px;height:91px;"></div>
  <div class="rule" style="left:0;top:92px;width:336px;"></div>
  <div class="brand brand--light" style="left:10px;top:28px;">
    <span class="brand__dot"></span>
    <span class="brand__name" style="font-size:14px;">Oak and River</span>
    <span class="brand__tagline">Learning &amp; Development</span>
  </div>
  <div class="faint-circle" role="img" aria-label="Faint brand symbol decoration" style="left:192px;top:440px;width:130px;height:130px;"></div>
  <div class="footer" style="top:620px;">
    41 Fennick Row · Marbury · North Wessex KX4 7RB · Registered Company no. 0000000<br>
    Phone 01000 000000 · Mobile 07000 000000 · mhollings@oakandriverltd-example.co.uk
  </div>
</section>

<section class="piece piece--black card" style="left:936px;top:252px;width:182px;height:103px;">
  <div class="brand brand--light brand--centre" style="left:0;right:0;top:28px;">
    <span class="brand__dot"></span>
    <span class="brand__name" style="font-size:12px;">Oak and River</span>
    <span class="brand__tagline">Learning &amp; Development</span>
  </div>
  <div class="rule" style="left:0;top:90px;width:182px;"></div>
</section>

<section class="piece piece--black card" style="left:936px;top:379px;width:182px;height:106px;">
  <div class="contact contact--light" style="left:12px;top:14px;">
    <div class="contact__name">Mara Hollings</div>
    <div class="contact__role">Director</div>
    <div>41 Fennick Row, Marbury</div>
    <div>North Wessex KX4 7RB</div>
    <div>Mobile 07000 000000</div>
    <div>mhollings@oakandriverltd-example.co.uk</div>
  </div>
  <div class="rule" style="left:0;top:92px;width:182px;"></div>
</section>
</body>
</html>
```